PowerPoint template for Law Firm

We Need a PowerPoint Template for a Law Firm in Switzerland. We are primarly consult in business law. We Need a template for PowerPoint to Show Information to our Clients (inheritence law, corporate law, legal structures etc.) The design should be contemporary, simple and clear. It should be in harmony with our website: www.trovanek.com Style: professional, structured and clearly arranged. Colors: Blue (R: 1, G: 61: B: 105), white. Font: Calibri Ratio: 16: 9 Esamples attached

```html
<!DOCTYPE html>
<html lang="en">
<head>
<meta charset="utf-8">
<title>Trovanek—Lawyers presentation template</title>
<link href="https://fonts.googleapis.com/css2?family=Carlito:wght@400;700&display=swap" rel="stylesheet">
<style>
  :root {
    --brand-blue: #013d69;
    --white: #ffffff;
    --ink: #111111;
    --ridge-light: rgba(255, 255, 255, 0.22);
    --ridge-fade: rgba(255, 255, 255, 0);
  }
  * { margin: 0; padding: 0; box-sizing: border-box; }
  html, body {
    width: 1200px; height: 710px; overflow: hidden;
    background: var(--white);
    font-family: "Carlito", Calibri, sans-serif;
  }
  .canvas { position: relative; width: 1200px; height: 710px; }

  .slide {
    position: absolute; width: 568px; height: 320px;
    background: var(--white);
  }
  .slide--tl { left: 24px; top: 28px; }
  .slide--tr { left: 610px; top: 28px; }
  .slide--bl { left: 24px; top: 365px; }
  .slide--br { left: 610px; top: 365px; }

  .slide__stage {
    position: absolute; left: 0; top: 0; width: 568px; height: 283px;
    background: var(--brand-blue); color: var(--white);
  }
  .slide--cover .slide__stage { height: 320px; }

  .slide__footer-url {
    position: absolute; left: 32px; top: 290px;
    font-size: 9px; color: var(--ink);
  }
  .slide__footer-name {
    position: absolute; right: 32px; top: 286px;
    font-size: 13.5px; color: var(--brand-blue); letter-spacing: 0.2px;
  }
  .slide__footer-bar {
    position: absolute; left: 0; bottom: 0; width: 568px; height: 8px;
    background: var(--brand-blue);
  }

  /* Cover */
  .cover__name {
    position: absolute; left: 0; width: 568px; top: 42px;
    text-align: center; font-size: 56px; font-weight: 400;
    letter-spacing: 1px; color: var(--white);
  }
  .cover__ridge {
    position: absolute; left: 29px; top: 228px; width: 502px; height: 64px;
    background:
      linear-gradient(90deg, var(--ridge-fade) 0%, var(--ridge-light) 12%, var(--ridge-light) 88%, var(--ridge-fade) 100%);
    -webkit-mask-image: linear-gradient(180deg, transparent 0%, #000 30%, #000 60%, transparent 100%);
    mask-image: linear-gradient(180deg, transparent 0%, #000 30%, #000 60%, transparent 100%);
  }

  /* Content slides */
  .slide__title {
    position: absolute; left: 0; width: 568px; top: 30px;
    text-align: center; font-weight: 700; font-size: 29px; line-height: 1;
  }
  .slide__subtitle {
    position: absolute; left: 0; width: 568px; top: 70px;
    text-align: center; font-weight: 700; font-size: 17px;
  }
  .photo-slot {
    position: absolute; background: var(--white); color: var(--ink);
    display: flex; align-items: center; justify-content: center;
    font-size: 10.5px;
  }
  .photo-slot--about-right { left: 39px; top: 101px; width: 215px; height: 141px; }
  .photo-slot--about-left { left: 316px; top: 100px; width: 216px; height: 141px; }
  .photo-slot--team {
    left: 27px; top: 76px; width: 249px; height: 169px;
    border: 1px solid var(--ink); font-size: 16.5px;
  }

  .body-copy {
    position: absolute; width: 258px;
    font-size: 10px; line-height: 12.9px; text-align: justify;
    text-transform: uppercase;
  }
  .body-copy p + p { margin-top: 12.9px; }
  .body-copy--right { left: 268px; top: 107px; }
  .body-copy--left { left: 43px; top: 106px; }

  .team__title {
    position: absolute; left: 0; width: 568px; top: 20px;
    text-align: center; font-weight: 700; font-size: 25px; line-height: 21px;
  }
  .team__lines {
    position: absolute; left: 297px; top: 102px;
    list-style: none; font-size: 14px; line-height: 21.4px;
  }
</style>
</head>
<body>
<main class="canvas">

  <section class="slide slide--tl slide--cover">
    <div class="slide__stage">
      <h1 class="cover__name">Trovanek—Lawyers</h1>
      <div class="cover__ridge" role="img" aria-label="Single-line drawing of a Swiss mountain ridge"></div>
    </div>
  </section>

  <section class="slide slide--tr">
    <div class="slide__stage">
      <h2 class="slide__title">ABOUT OUR FIRM</h2>
      <h3 class="slide__subtitle">SUB-TITLE</h3>
      <div class="photo-slot photo-slot--about-right">INSERT PHOTO HERE</div>
      <div class="body-copy body-copy--right">
        <p>Example text: put anything you want to say about the company.</p>
        <p>Sample text only. Sample text only. Sample text only. Sample text only. Sample text only. Sample text only. Sample text only. Sample text only. Sample text only. Sample text only. Sample text only. Sample text only. Sample text only. Sample text only. Sample text only. Sample text only. Sample text only.</p>
      </div>
    </div>
    <span class="slide__footer-url">www.trovanek.com</span>
    <span class="slide__footer-name">Trovanek—Lawyers</span>
    <div class="slide__footer-bar"></div>
  </section>

  <section class="slide slide--bl">
    <div class="slide__stage">
      <h2 class="slide__title">ABOUT OUR FIRM</h2>
      <h3 class="slide__subtitle">SUB-TITLE</h3>
      <div class="body-copy body-copy--left">
        <p>Example text: put anything you want to say about the company.</p>
        <p>Sample text only. Sample text only. Sample text only. Sample text only. Sample text only. Sample text only. Sample text only. Sample text only. Sample text only. Sample text only. Sample text only. Sample text only. Sample text only. Sample text only. Sample text only. Sample text only. Sample text only.</p>
      </div>
      <div class="photo-slot photo-slot--about-left">INSERT PHOTO HERE</div>
    </div>
    <span class="slide__footer-url">www.trovanek.com</span>
    <span class="slide__footer-name">Trovanek—Lawyers</span>
    <div class="slide__footer-bar"></div>
  </section>

  <section class="slide slide--br">
    <div class="slide__stage">
      <h2 class="team__title">MEET OUR<br>TEAM/FOUNDER</h2>
      <div class="photo-slot photo-slot--team">INSERT PHOTO HERE</div>
      <ul class="team__lines">
        <li>Sample text only. Sample text only.</li>
        <li>Sample text only. Sample text only.</li>
        <li>Sample text only. Sample text only.</li>
        <li>Sample text only. Sample text only.</li>
        <li>Sample text only. Sample text only.</li>
      </ul>
    </div>
    <span class="slide__footer-url">www.trovanek.com</span>
    <span class="slide__footer-name">Trovanek—Lawyers</span>
    <div class="slide__footer-bar"></div>
  </section>

</main>
</body>
</html>
```